Need stationery and business card design for Appraisal Company
Stonewell Valuations & Advisory
Professional
Lonny Harwick
Certified Residential Appraiser
5182 W Maple Ct.
Redmesa, AZ 85390
lonny@stonewellvaluations.example
Business logo and font will be uploaded.

```html
<!DOCTYPE html>
<html lang="en">
<head>
<meta charset="utf-8">
<title>Stonewell Valuations &amp; Advisory — Business Card</title>
<link rel="stylesheet" href="https://fonts.googleapis.com/css2?family=Cinzel:wght@400;600&display=swap">
<style>
  :root {
    --page-bg: #e9e6e2;
    --card-white: #ffffff;
    --brand-red: #ef3b24;
    --brand-red-deep: #d92a16;
    --swoosh-black: #1c1c1c;
    --ink-dark: #2b2b2b;
    --ink-light: #ffffff;
  }
  * { margin: 0; padding: 0; box-sizing: border-box; }
  html, body {
    width: 1200px; height: 914px; overflow: hidden;
    background: var(--page-bg);
  }
  .canvas {
    position: relative; width: 1200px; height: 914px;
    display: flex; align-items: center; justify-content: center;
  }
  .business-card {
    position: relative; width: 1000px; height: 572px;
    background: var(--card-white);
    box-shadow: 0 18px 40px rgba(0,0,0,0.22);
    overflow: hidden;
    font-family: "Cinzel", serif;
  }
  .card-waves { position: absolute; inset: 0; }
  .brand-lockup {
    position: absolute; top: 140px; left: 0; right: 0;
    display: flex; align-items: center; justify-content: center; gap: 16px;
  }
  .brand-mark {
    width: 22px; height: 22px; background: var(--brand-red);
  }
  .brand-name {
    font-family: "Cinzel", serif; font-weight: 600;
    font-size: 36px; letter-spacing: 2px; color: var(--ink-dark);
  }
  .card-details {
    position: absolute; left: 0; right: 0; top: 380px;
    display: flex; justify-content: center; color: var(--ink-light);
  }
  .person {
    width: 420px; text-align: right; padding-right: 28px; padding-top: 6px;
  }
  .person-name { font-size: 24px; letter-spacing: 1px; }
  .person-title { font-size: 17px; margin-top: 8px; letter-spacing: 0.5px; }
  .divider { width: 2px; height: 150px; background: rgba(255,255,255,0.8); }
  .contact-list { list-style: none; padding-left: 24px; width: 440px; }
  .contact-item {
    display: flex; align-items: center; gap: 12px;
    font-size: 15px; line-height: 1; height: 26px; letter-spacing: 0.3px;
  }
  .contact-item.indent { padding-left: 32px; }
  .contact-icon { width: 20px; height: 20px; flex: none; }
</style>
</head>
<body>
<main class="canvas">
  <article class="business-card">
    <svg class="card-waves" viewBox="0 0 1000 572" preserveAspectRatio="none" aria-hidden="true">
      <path d="M0 270 C 250 215, 500 330, 1000 200 L1000 572 L0 572 Z" fill="var(--swoosh-black)"/>
      <path d="M0 292 C 260 240, 520 350, 1000 222 L1000 572 L0 572 Z" fill="var(--card-white)"/>
      <path d="M0 304 C 260 256, 520 364, 1000 234 L1000 572 L0 572 Z" fill="var(--brand-red)"/>
      <path d="M0 572 L0 470 C 300 520, 700 440, 1000 480 L1000 572 Z" fill="var(--brand-red-deep)" opacity="0.35"/>
    </svg>

    <div class="brand-lockup">
      <span class="brand-mark"></span>
      <span class="brand-name">Stonewell Valuations &amp; Advisory</span>
    </div>

    <section class="card-details">
      <div class="person">
        <p class="person-name">Lonny Harwick</p>
        <p class="person-title">Certified Residential Appraiser</p>
      </div>
      <div class="divider"></div>
      <ul class="contact-list">
        <li class="contact-item">
          <svg class="contact-icon" viewBox="0 0 20 20" aria-hidden="true"><circle cx="10" cy="10" r="10" fill="#fff"/><path d="M10 4a4 4 0 0 0-4 4c0 3 4 8 4 8s4-5 4-8a4 4 0 0 0-4-4zm0 5.5a1.5 1.5 0 1 1 0-3 1.5 1.5 0 0 1 0 3z" fill="var(--brand-red)"/></svg>
          5182 W Maple Ct.
        </li>
        <li class="contact-item indent">Redmesa, AZ 85390</li>
        <li class="contact-item">
          <svg class="contact-icon" viewBox="0 0 20 20" aria-hidden="true"><circle cx="10" cy="10" r="10" fill="#fff"/><path d="M7 5l2 3-1.2 1.2a7 7 0 0 0 3 3L12 11l3 2-1 2c-4 0-8-4-8-8z" fill="var(--brand-red)"/></svg>
          480-555-0147
        </li>
        <li class="contact-item">
          <svg class="contact-icon" viewBox="0 0 20 20" aria-hidden="true"><circle cx="10" cy="10" r="10" fill="#fff"/><rect x="5" y="6.5" width="10" height="7" fill="var(--brand-red)"/><path d="M5 6.5l5 4 5-4" stroke="#fff" stroke-width="1" fill="none"/></svg>
          lonny@stonewellvaluations.example
        </li>
        <li class="contact-item">
          <svg class="contact-icon" viewBox="0 0 20 20" aria-hidden="true"><circle cx="10" cy="10" r="10" fill="#fff"/><circle cx="10" cy="10" r="5" fill="none" stroke="var(--brand-red)" stroke-width="1.3"/><path d="M5 10h10M10 5c-2 3-2 7 0 10M10 5c2 3 2 7 0 10" stroke="var(--brand-red)" stroke-width="1" fill="none"/></svg>
          www.stonewellvaluations.example
        </li>
      </ul>
    </section>
  </article>
</main>
</body>
</html>
```